Letter Head Design - Finance industry

Design a letterhead to match the logo. Needs to be clean, simple and crisp. I'm open to suggestions. Will be using the logo that was submitted last with the W crossed over

Target Market(s)

Small medium businesses and government department's

Industry/Entity Type

Industry

Font styles to use
Sans Serif

Colors
cadf82
bcd85c
acd036
9bcb3c
e9e9e9
aaaaaa
000000
7f7f7f
b7b7b7

Requirements
Must have
• Need to display: Logo, Business address, ABN number, ASIC register number, contact phone, website, company email. Details are as per below:

Suite 4B Level 17
Marlowe Harbour Tower
9 Tindall Place
Sydney NSW 2000
Landline Ph: 02 5193 2604
Ph: 1300 4917 63
Email: enquiries@brightmoorfin.com.au
W: www.brightmoorfin.com.au

On the footer, the details below need to be specified:
ABN: 43 719 385 207
ASIC Registration Number: 27 318640571

Should not have
• No imagery or design that is not in line with the logo

```html
<!DOCTYPE html>
<html lang="en">
<head>
<meta charset="utf-8">
<title>Brightmoor Finance — Letterhead</title>
<link href="https://fonts.googleapis.com/css2?family=Open+Sans:wght@400;600&display=swap" rel="stylesheet">
<style>
  :root {
    --green-light: #cadf82;
    --green: #acd036;
    --green-deep: #9bcb3c;
    --grey-pale: #e9e9e9;
    --grey-mid: #aaaaaa;
    --grey-text: #7f7f7f;
    --grey-line: #b7b7b7;
    --ink: #000000;
    --backdrop: #e4e4e4;
    --paper: #f8f8f8;
    --watermark: #ededed;
  }
  * { margin: 0; padding: 0; box-sizing: border-box; }
  html, body {
    width: 1200px; height: 1000px; overflow: hidden;
    background: var(--backdrop);
    font-family: "Open Sans", Arial, sans-serif;
  }
  .letterhead {
    position: absolute; left: 250px; top: 0;
    width: 700px; height: 1000px;
    background: var(--paper);
  }
  .brand {
    position: absolute; left: 80px; top: 66px;
    display: flex; align-items: center; gap: 12px;
  }
  .brand-dot {
    width: 36px; height: 36px; border-radius: 50%;
    background: var(--green-deep);
  }
  .brand-name {
    font-size: 26px; font-weight: 400; line-height: 1.05;
    color: var(--grey-text);
  }
  .contact {
    position: absolute; left: 472px; top: 82px;
    list-style: none;
    font-size: 7.5px; line-height: 10.5px; color: #222;
  }
  .contact li { display: flex; align-items: flex-start; gap: 5px; }
  .contact svg { width: 7px; height: 7px; margin-top: 1.5px; flex: none; fill: var(--green-deep); }
  .contact .indent { padding-left: 12px; }
  .contact .label { font-weight: 600; }
  .watermark {
    position: absolute; left: 232px; top: 424px;
    width: 236px; height: 236px;
  }
  .footer {
    position: absolute; left: 263px; top: 946px;
    width: 174px;
    border-top: 1px solid var(--grey-line);
    padding-top: 7px;
    font-size: 7.5px; font-weight: 600; color: #222;
    white-space: nowrap;
  }
  .footer .key { color: var(--green); }
  .footer .sep { margin: 0 4px; }
</style>
</head>
<body>
  <main class="letterhead">
    <header>
      <div class="brand">
        <span class="brand-dot"></span>
        <span class="brand-name">Brightmoor<br>Finance</span>
      </div>
      <ul class="contact">
        <li>
          <svg viewBox="0 0 10 10"><path d="M5 0a3.5 3.5 0 0 0-3.5 3.5C1.5 6 5 10 5 10s3.5-4 3.5-6.5A3.5 3.5 0 0 0 5 0zm0 5a1.5 1.5 0 1 1 0-3 1.5 1.5 0 0 1 0 3z"/></svg>
          <span>Suite 4B Level 17, Marlowe Harbour Tower</span>
        </li>
        <li class="indent">9 Tindall Place, Sydney NSW 2000</li>
        <li>
          <svg viewBox="0 0 10 10"><path d="M2 0l2 2.5-1.2 1.3a6 6 0 0 0 3.4 3.4L7.5 6 10 8l-1.5 2C4 10 0 6 0 1.5z"/></svg>
          <span><span class="label">(Landline)</span> 02 5193 2604 / 1300 4917 63</span>
        </li>
        <li>
          <svg viewBox="0 0 10 10"><rect x="0" y="1.5" width="10" height="7" rx="1"/><path d="M0.5 2l4.5 3.5L9.5 2" fill="none" stroke="#f8f8f8" stroke-width="1"/></svg>
          <span>enquiries@brightmoorfin.com.au</span>
        </li>
        <li>
          <svg viewBox="0 0 10 10"><circle cx="5" cy="5" r="5"/><path d="M0 5h10M5 0c-2.5 2.8-2.5 7.2 0 10M5 0c2.5 2.8 2.5 7.2 0 10" fill="none" stroke="#f8f8f8" stroke-width="0.8"/></svg>
          <span>www.brightmoorfin.com.au</span>
        </li>
      </ul>
    </header>

    <svg class="watermark" viewBox="0 0 236 236" aria-hidden="true">
      <circle cx="118" cy="118" r="118" fill="var(--watermark)"/>
    </svg>

    <footer class="footer">
      <span class="key">ABN:</span> 43 719 385 207<span class="sep">|</span><span class="key">ASIC:</span> 27 318640571
    </footer>
  </main>
</body>
</html>
```